Administrative services outsourcing needs a website design

We need a website design for a new company based out of Nashville TN called Corvanel Employer Services.
Corvanel Employer Services is a ASO that offers the ultimate solution for businesses looking for administrative relief and professional management of their employment and Human Resource practices. By integrating payroll, employee benefits, 401(k) plan requirements and employment administration into a streamlined and efficient system that results in a single point of delivery, our clients can reallocate internal resources toward more strategic initiatives that drive better business results.
Updates

Project Deadline Extended
Reason: Give the designers more time to present.

Target Market(s)

Employers

Industry/Entity Type

It Company

Number of Pages Required

5+ page

Requirements
Must have
• Combination of these 2 websites
• corvanel.example
• trilbowen.example
• slogan="Right engine, right time, right price"

```html
<!DOCTYPE html>
<html lang="en">
<head>
<meta charset="utf-8">
<title>Corvanel Employer Services</title>
<link href="https://fonts.googleapis.com/css2?family=Hind:wght@300;400;500&display=swap" rel="stylesheet">
<style>
:root{
  --green:#4fa82a;
  --green-dark:#3c8c1c;
  --ink:#222;
  --text:#555;
  --muted:#777;
  --rule:#e4e4e4;
  --bg:#fff;
}
*{box-sizing:border-box;margin:0;padding:0}
html,body{width:906px;height:1200px;overflow:hidden;background:var(--bg)}
body{position:relative;font-family:"Hind",Arial,sans-serif;color:var(--text)}
.abs{position:absolute}
.brand{left:74px;top:38px;display:flex;align-items:center;gap:8px}
.brand-dot{width:22px;height:22px;border-radius:50%;background:var(--green)}
.brand-name{font-size:17px;font-weight:500;color:var(--ink);line-height:1.1;width:120px}
.address{right:74px;top:24px;font-size:10px;color:#444}
.phone{right:74px;top:49px;font-size:17px;color:var(--green);display:flex;align-items:center;gap:6px}
.main-nav{right:74px;top:85px;display:flex;gap:29px;font-size:13px;color:var(--ink)}
.main-nav .active,.foot-nav .active{color:var(--green)}
.hero{left:0;top:121px;width:906px;height:370px;background:linear-gradient(100deg,#cfd2d3 0%,#b8b3ab 35%,#4a5566 60%,#2a3242 80%,#b7b1a6 100%)}
.slogan{left:74px;top:262px;font-size:33px;line-height:37px;color:#1a1a1a;font-weight:400;width:400px}
.dots{left:74px;top:355px;display:flex;gap:6px}
.dots span{width:7px;height:7px;border-radius:50%;background:#bbb}
.dots span:first-child{background:var(--green)}
.section-title{font-size:25px;color:var(--ink);font-weight:400}
.services{left:74px;top:577px;display:flex;gap:8px}
.service{width:145px}
.service-photo{height:67px;background:linear-gradient(135deg,#5c6e87,#c9ccd0)}
.service h3{font-size:13px;font-weight:400;color:var(--green);margin-top:14px}
.service p{font-size:9px;line-height:15.5px;margin-top:6px;color:#555}
.divider{left:80px;top:757px;width:746px;height:12px;background:radial-gradient(ellipse at top,rgba(0,0,0,.12),rgba(0,0,0,0) 70%)}
.screen{left:74px;top:853px;width:195px;height:143px;background:linear-gradient(90deg,#3f8f1c 0 22%,#f2f2f2 22%);border:1px solid #ddd;box-shadow:0 6px 14px rgba(0,0,0,.15)}
.body-copy{font-size:9.7px;line-height:15.6px;color:#555}
.cta-links{left:291px;top:1003px;font-size:12px;line-height:19px;color:var(--green)}
.checks{left:520px;top:956px;list-style:none;font-size:10px;color:#333}
.checks li{display:flex;align-items:center;gap:11px;height:23.3px}
.btn{left:521px;top:1083px;width:62px;height:25px;background:var(--green);color:#fff;font-size:9.5px;display:flex;align-items:center;justify-content:center;border-radius:2px}
.foot-rule{left:74px;top:1136px;width:758px;height:1px;background:var(--rule)}
.foot-nav{left:73px;top:1149px;display:flex;gap:30px;font-size:12.5px;color:var(--ink)}
.copyright{left:74px;top:1173px;font-size:9px;color:var(--muted)}
.social{left:752px;top:1149px;display:flex;gap:5px}
.social span{width:23px;height:23px;border-radius:50%;border:2px solid #ddd}
.social .s1{background:#3b5a96}.social .s2{background:#2a9fd8}.social .s3{background:#c93a2c}
</style>
</head>
<body>
<header>
  <div class="abs brand"><span class="brand-dot"></span><span class="brand-name">Corvanel Employer Services</span></div>
  <div class="abs address">48 Larkmoor Avenue, Suite C210, Franklin, TN 37000</div>
  <div class="abs phone">
    <svg width="13" height="13" viewBox="0 0 13 13"><rect width="13" height="13" rx="2" fill="#4fa82a"/><path d="M4 3c.6 0 1 1.6 1 2s-.7.6-.5 1.1 1.3 1.9 2 2.1.6-.5 1.1-.5 2 .4 2 1-.9 1.3-1.6 1.3C5.5 10 3 7.5 3 4.4 3 3.6 3.5 3 4 3z" fill="#fff"/></svg>
    615-555-0142
  </div>
  <nav class="abs main-nav"><span class="active">Home</span><span>Why Corvanel</span><span>Services</span><span>Financial Advisors</span><span>Contact</span><span>Blog</span></nav>
</header>

<section>
  <div class="abs hero" role="img" aria-label="Photo of two smiling businessmen in suits looking at a laptop"></div>
  <h1 class="abs slogan">Right engine, Right time, Right price</h1>
  <div class="abs dots"><span></span><span></span><span></span></div>
</section>

<section>
  <h2 class="abs section-title" style="left:74px;top:522px">Our Services</h2>
  <div class="abs services">
    <div class="service"><div class="service-photo" role="img" aria-label="Photo of a team working around a laptop"></div><h3>Employer Consulting</h3><p>Nemo enim ipsam voluptatem quia voluptas sit aspernatur aut odit aut fugit, sed quia...</p></div>
    <div class="service"><div class="service-photo" role="img" aria-label="Photo of colleagues in a meeting"></div><h3>HR Consulting</h3><p>Nemo enim ipsam voluptatem quia voluptas sit aspernatur aut odit aut fugit, sed quia...</p></div>
    <div class="service"><div class="service-photo" role="img" aria-label="Photo of a smiling office team"></div><h3>Payroll Services</h3><p>Nemo enim ipsam voluptatem quia voluptas sit aspernatur aut odit aut fugit, sed quia...</p></div>
    <div class="service"><div class="service-photo" role="img" aria-label="Photo of a man working on a laptop"></div><h3>Paperless Onboarding</h3><p>Nemo enim ipsam voluptatem quia voluptas sit aspernatur aut odit aut fugit, sed quia...</p></div>
    <div class="service"><div class="service-photo" style="background:linear-gradient(135deg,#2a2a2c,#6d6f74)" role="img" aria-label="Photo of a man checking his wristwatch"></div><h3>Applicant Tracking</h3><p>Nemo enim ipsam voluptatem quia voluptas sit aspernatur aut odit aut fugit, sed quia...</p></div>
  </div>
</section>

<div class="abs divider"></div>

<section>
  <h2 class="abs section-title" style="left:73px;top:793px;font-size:24px">Let us Administer your 401(k).</h2>
  <div class="abs screen" role="img" aria-label="Screenshot of an employee list in the payroll software"></div>
  <p class="abs body-copy" style="left:291px;top:850px;width:205px">Corvanel understands the challenges of running a business, but HR doesn't need to be one of them. With our HR Consulting Services, you can outsource your entire HR department or fill missing skill gaps by choosing just the service offerings that suit your needs. We are an independent, compliance-driven HR solution. From needing a little advice to developing a full human resources system, we're here to help.</p>
  <div class="abs cta-links">HR Questions? We're on call.<br>PayLoom. More than Payroll Processing.</div>
</section>

<section>
  <h2 class="abs section-title" style="left:519px;top:800px">Employer Services Consulting</h2>
  <p class="abs body-copy" style="left:520px;top:850px;width:314px">Thanks for stopping by our new website and learning about our blog. During the coming weeks, we'll be writing on topics relevant to Human Capital Management and trends in HCM technologies. Now more than ever, human resources professionals must do more with less. By automating manual processes and eliminating paper, organizations can gain a significant ROI. Our blog topics will include:</p>
  <ul class="abs checks">
    <li><svg width="9" height="8" viewBox="0 0 9 8"><path d="M1 4l2.5 2.5L8 1" stroke="#222" stroke-width="2" fill="none"/></svg>Employee Onboarding</li>
    <li><svg width="9" height="8" viewBox="0 0 9 8"><path d="M1 4l2.5 2.5L8 1" stroke="#222" stroke-width="2" fill="none"/></svg>Applicant Tracking Systems</li>
    <li><svg width="9" height="8" viewBox="0 0 9 8"><path d="M1 4l2.5 2.5L8 1" stroke="#222" stroke-width="2" fill="none"/></svg>Payroll Services</li>
    <li><svg width="9" height="8" viewBox="0 0 9 8"><path d="M1 4l2.5 2.5L8 1" stroke="#222" stroke-width="2" fill="none"/></svg>Benefits Technology</li>
    <li><svg width="9" height="8" viewBox="0 0 9 8"><path d="M1 4l2.5 2.5L8 1" stroke="#222" stroke-width="2" fill="none"/></svg>HCM Technology</li>
  </ul>
  <div class="abs btn">Read More</div>
</section>

<footer>
  <div class="abs foot-rule"></div>
  <nav class="abs foot-nav"><span class="active">Home</span><span>Why Corvanel</span><span>Services</span><span>Financial Advisors</span><span>Contact</span><span>Blog</span></nav>
  <div class="abs copyright">© 2015 Quillmark Studio. All rights reserved.</div>
  <div class="abs social"><span class="s1"></span><span class="s2"></span><span class="s3"></span></div>
</footer>
</body>
</html>
```